Building Servicess

We need a new business card design for a company. We specialise in: Electrical/Site temporary electrics, Data/Network Installation, Passive Fire Protection

Industry/Entity Type

Construction

Contact Information for Business Card

Services provided as detailed on project description

Font styles to use
Serif

Colors
0054AA
0677BA
7BADD7
CADEEF
E8F1F8
00AB8E
00BBA5
67D7C9
C6EFE9
E9F9F6
EB3D1F
EC4F4E
F09395
F8D3D4
FCEDEE

Requirements
Must have
• Company logo-contact details-phone numbers

```html
<!DOCTYPE html>
<html lang="en">
<head>
<meta charset="utf-8">
<title>Corvane Site Services – Business Card</title>
<link rel="stylesheet" href="https://fonts.googleapis.com/css2?family=Montserrat:wght@400;500;600;700&display=swap">
<style>
  :root {
    --page-bg: #e7e8ea;
    --brand-blue: #1256a8;
    --brand-blue-light: #1a62b4;
    --brand-mid: #0677ba;
    --paper: #ffffff;
    --ink-light: #ffffff;
  }
  * { margin: 0; padding: 0; box-sizing: border-box; }
  html, body {
    width: 1200px; height: 1000px; overflow: hidden;
    background: var(--page-bg);
    font-family: "Montserrat", Arial, sans-serif;
  }
  .canvas { position: relative; width: 1200px; height: 1000px; }

  .card { position: absolute; left: 311px; width: 579px; height: 331px; overflow: hidden; }

  /* Front */
  .card--front { top: 120px; background: var(--brand-blue); }
  .front__pattern { position: absolute; inset: 0; background: var(--brand-blue); }
  .front__brand {
    position: absolute; left: 0; right: 0; top: 132px;
    text-align: center; color: var(--ink-light);
    font-weight: 700; line-height: 1.05;
  }
  .front__brand-name { font-size: 44px; letter-spacing: 3px; display: block; }
  .front__brand-sub { font-size: 18px; letter-spacing: 2px; display: block; margin-top: 8px; }
  .front__services {
    position: absolute; left: 0; right: 0; top: 265px;
    text-align: center; color: var(--ink-light);
    font-size: 13px; font-weight: 400; letter-spacing: 0.4px; line-height: 20px;
  }
  .front__services .divider {
    display: inline-block; width: 2px; height: 14px; background: var(--ink-light);
    vertical-align: -2px; margin: 0 18px 0 20px;
  }

  /* Back */
  .card--back { top: 550px; background: var(--paper); }
  .back__brand-panel {
    position: absolute; left: 0; top: 0; width: 277px; height: 100%;
    display: flex; flex-direction: column; align-items: center; justify-content: center;
    color: var(--brand-blue); font-weight: 700; text-align: center; line-height: 1.1;
  }
  .back__brand-name { font-size: 30px; letter-spacing: 2px; }
  .back__brand-sub { font-size: 12px; letter-spacing: 1.5px; margin-top: 6px; }
  .back__info {
    position: absolute; left: 277px; top: 0; right: 0; height: 100%;
    background: var(--brand-blue); color: var(--ink-light);
  }
  .person__name { position: absolute; left: 13px; top: 70px; font-size: 20px; font-weight: 700; letter-spacing: 0.6px; }
  .person__role { position: absolute; left: 13px; top: 97px; font-size: 12.5px; font-weight: 500; letter-spacing: 0.5px; }
  .contact__rule { position: absolute; left: 9px; top: 168px; width: 2px; height: 111px; background: var(--ink-light); }
  .contact__list { position: absolute; left: 18px; top: 165px; list-style: none; font-size: 15px; font-weight: 400; }
  .contact__item { display: flex; align-items: flex-start; line-height: 22px; margin-bottom: 4px; }
  .contact__icon { width: 14px; height: 14px; margin: 4px 8px 0 0; flex: none; fill: var(--ink-light); }
</style>
</head>
<body>
<main class="canvas">

  <section class="card card--front">
    <div class="front__pattern" role="img" aria-label="Faint repeating brand mark pattern across the card background"></div>
    <div class="front__brand">
      <span class="front__brand-name">CORVANE</span>
      <span class="front__brand-sub">SITE SERVICES LTD</span>
    </div>
    <p class="front__services">
      ELECTRICAL/SITE TEMPORARY ELECTRICS<br>
      DATA/NETWORK INSTALLATION<span class="divider"></span>PASSIVE FIRE PROTECTION
    </p>
  </section>

  <section class="card card--back">
    <div class="back__brand-panel">
      <span class="back__brand-name">CORVANE</span>
      <span class="back__brand-sub">SITE SERVICES LTD</span>
    </div>
    <div class="back__info">
      <h1 class="person__name">DANIEL ASHWORTH</h1>
      <p class="person__role">MANAGING DIRECTOR</p>
      <span class="contact__rule"></span>
      <ul class="contact__list">
        <li class="contact__item">
          <svg class="contact__icon" viewBox="0 0 24 24"><path d="M6.6 10.8a15.1 15.1 0 0 0 6.6 6.6l2.2-2.2c.3-.3.7-.4 1-.2 1.1.4 2.3.6 3.6.6.6 0 1 .4 1 1V20c0 .6-.4 1-1 1A17 17 0 0 1 3 4c0-.6.4-1 1-1h3.5c.6 0 1 .4 1 1 0 1.3.2 2.5.6 3.6.1.3 0 .7-.2 1z"/></svg>
          020 7946 0381
        </li>
        <li class="contact__item">
          <svg class="contact__icon" viewBox="0 0 24 24"><path d="M7 1h10a2 2 0 0 1 2 2v18a2 2 0 0 1-2 2H7a2 2 0 0 1-2-2V3a2 2 0 0 1 2-2zm0 3v14h10V4zm5 15.5a1 1 0 1 0 0 2 1 1 0 0 0 0-2z"/></svg>
          07700900415
        </li>
        <li class="contact__item">
          <svg class="contact__icon" viewBox="0 0 24 24"><path d="M12 2a10 10 0 1 0 0 20 10 10 0 0 0 0-20zm6.9 6h-2.9a15.6 15.6 0 0 0-1.4-3.6A8 8 0 0 1 18.9 8zM12 4c.8 1.2 1.5 2.5 1.9 4h-3.8c.4-1.5 1.1-2.8 1.9-4zM4.3 14a8.2 8.2 0 0 1 0-4h3.4a16.5 16.5 0 0 0 0 4zm.8 2h2.9c.3 1.3.8 2.5 1.4 3.6A8 8 0 0 1 5.1 16zM8 8H5.1a8 8 0 0 1 4.3-3.6C8.8 5.5 8.3 6.7 8 8zm4 12c-.8-1.2-1.5-2.5-1.9-4h3.8c-.4 1.5-1.1 2.8-1.9 4zm2.3-6H9.7a14.7 14.7 0 0 1 0-4h4.6a14.7 14.7 0 0 1 0 4zm.3 5.6c.6-1.1 1.1-2.3 1.4-3.6h2.9a8 8 0 0 1-4.3 3.6zm1.7-5.6a16.5 16.5 0 0 0 0-4h3.4a8.2 8.2 0 0 1 0 4z"/></svg>
          corvaneservices.co.uk
        </li>
        <li class="contact__item">
          <svg class="contact__icon" viewBox="0 0 24 24"><path d="M12 2a7 7 0 0 0-7 7c0 5.2 7 13 7 13s7-7.8 7-13a7 7 0 0 0-7-7zm0 9.5a2.5 2.5 0 1 1 0-5 2.5 2.5 0 0 1 0 5z"/></svg>
          <span>Meadow Lane, Brentwood,<br>Essex, CM14 5QR</span>
        </li>
      </ul>
    </div>
  </section>

</main>
</body>
</html>
```